Broschüre für eine Trainingsakademie
Zielgruppe
Ich möchte eine Broschüre zu meinem Unternehmen und meinen Angeboten schöner Design haben.
Ich bin Trainer/ Coach für moderne Personalstrategien insbesondere für die Personalgewinnung, Mitarbeiterbindung und -entwicklung. Zudem biete ich Trainings und Coachings für Mitarbeiter und Führungskräfte an. Zum Beispiel zu Themen wie gesunde Führung, Stressmanagement, Resilienz usw.
Meine Zielgruppe sind vor allem mittelständische Unternehmen oder junge aufstrebende StartUps, die ich beim Aufbau von Personalstrukturen unterstütze.
Aufgabenstellung
Mein Logo und die Farben sollen entsprechend berücksichtigt werden. Ein Entwurf für die Broschüre besteht bereits. Das ist allerdings nur meine Idee, als Laie. Ich hätte hier gern professionelle Ideen, so dass die Broschüre professionell und ansprechend wirkt.
Bilder habe ich eigentlich - diese finden sich auch auf meiner Homepage. Allerdings bin ich gerade auch beim Deckblatt offen. Auch für andere Gestaltungsvorschläge.

```html
<!DOCTYPE html>
<html lang="de">
<head>
<meta charset="utf-8">
<title>Velmora Coaching – Broschüre Seiten 10 und 11</title>
<link href="https://fonts.googleapis.com/css2?family=Arimo:wght@400;500&display=swap" rel="stylesheet">
<style>
  :root {
    --backdrop: #ecebf0;
    --paper: #ffffff;
    --ink: #23222c;
    --violet: #4f4675;
    --violet-soft: #8d7fb8;
    --lavender: #cfcbdc;
    --lavender-pale: #ebe9f1;
    --folio: #a9a5b9;
    --rule: #5b5384;
  }
  * { margin: 0; padding: 0; box-sizing: border-box; }
  html, body { width: 1200px; height: 600px; overflow: hidden; }
  body {
    background: var(--backdrop);
    font-family: "Arimo", Arial, sans-serif;
    color: var(--ink);
    position: relative;
  }
  .page {
    position: absolute;
    width: 549px;
    height: 387px;
    background: var(--paper);
    border: 1px solid #3a3a44;
    overflow: hidden;
  }
  .page--left { left: 27px; top: 28px; }
  .page--right { left: 622px; top: 184px; }

  .corner-bands { position: absolute; left: 0; top: 0; width: 150px; height: 160px; }

  .brand-name {
    position: absolute;
    left: 397px; top: 40px;
    width: 115px;
    text-align: center;
    font-size: 14px;
    font-weight: 500;
    letter-spacing: 0.5px;
    color: var(--violet);
    line-height: 18px;
  }

  .intro {
    position: absolute;
    left: 41px; top: 36px;
    width: 218px;
    font-size: 9.6px;
    line-height: 13px;
    text-align: justify;
  }
  .body-copy {
    position: absolute;
    left: 41px; top: 147px;
    width: 466px;
    font-size: 9.6px;
    line-height: 13px;
  }
  .body-copy p + p { margin-top: 13px; }

  .art { position: absolute; }
  .art--climber { left: 280px; top: 0; width: 53px; height: 105px;
    background: linear-gradient(180deg, #6a5f90, #4a4268); }
  .art--landscape { left: 367px; top: 73px; width: 141px; height: 52px;
    background: linear-gradient(180deg, #a79cc8, #8577b3); }
  .art--stepper { left: 458px; top: 293px; width: 30px; height: 94px;
    background: linear-gradient(180deg, #5a5080, #463f63); }

  .tagline-rule-h { position: absolute; left: 0; top: 293px; width: 293px; height: 1px; background: var(--rule); }
  .tagline-rule-v { position: absolute; left: 28px; top: 275px; width: 1px; height: 80px; background: var(--rule); }
  .tagline-glow { position: absolute; left: 29px; top: 294px; width: 264px; height: 30px;
    background: linear-gradient(180deg, var(--lavender-pale), rgba(255,255,255,0)); }
  .tagline { position: absolute; left: 41px; top: 300px; font-size: 11px; line-height: 16px; }
  .tagline__big { font-size: 15.5px; }
  .tagline__line + .tagline__line { margin-top: 2px; }

  .folio {
    position: absolute;
    left: 488px; top: 354px;
    width: 20px; height: 33px;
    background: var(--folio);
    color: #fff;
    font-size: 11px;
    text-align: center;
    padding-top: 7px;
  }

  .contact {
    position: absolute;
    left: 41px; top: 37px;
    font-size: 9.6px;
    line-height: 13px;
  }
  .contact__group + .contact__group { margin-top: 13px; }
</style>
</head>
<body>

<section class="page page--left">
  <svg class="corner-bands" viewBox="0 0 150 160" aria-hidden="true">
    <defs>
      <linearGradient id="bandFade" x1="0" y1="0" x2="0.3" y2="1">
        <stop offset="0" stop-color="#c9c5d9"/>
        <stop offset="1" stop-color="#ffffff" stop-opacity="0"/>
      </linearGradient>
    </defs>
    <polygon points="0,0 20,0 95,75 0,150" fill="url(#bandFade)"/>
    <polygon points="30,0 60,0 140,80 60,160 0,160 0,140 60,80" fill="url(#bandFade)" opacity="0.8"/>
  </svg>

  <div class="brand-name">Velmora Coaching</div>

  <p class="intro">Mitten in der schönen Lüneburger Heide zwischen Hamburg, Hannover und Bremen ist der Sitz von Velmora Coaching. Hier wird immer am Zahn der Zeit neues Wissen, neue Forschungsergebnisse und Trends aus dem Personalmanagement gebündelt und für die Kunden aufbereitet, damit Sie immer die beste Beratung erhalten!</p>

  <div class="art art--climber" role="img" aria-label="Illustration: Figur, die eine Leiter hinaufsteigt"></div>
  <div class="art art--landscape" role="img" aria-label="Illustration: kleine Figur vor einer violetten Heidelandschaft"></div>

  <div class="body-copy">
    <p>Digital oder in Präsenz - in einzelnen Modulen oder als Tagestrainings - Inhouse oder Seminarhotel:</p>
    <p>Die Coachings und Trainings werden entsprechend den Anforderungen und Bedürfnissen der Auftraggeber konzipiert! Der persönliche Kontakt und Austausch wird in Präsenztrainings besonders geschätzt. Dies eignet sich vor allem für Auftaktveranstaltungen oder mehrtägigen Ganztagestrainings in Gruppen. Nutzen Sie die Vorteile virtueller Trainings und Coaching für das modulare Training und individuelle Coaching sowie die Umsetzungsbegleitung.</p>
    <p>Infomieren Sie sich jetzt und erhalten Sie ein maßgeschneidertes Angebot!</p>
  </div>

  <div class="tagline-glow"></div>
  <div class="tagline-rule-h"></div>
  <div class="tagline-rule-v"></div>
  <div class="tagline">
    <div class="tagline__line">„Velmora Coaching“</div>
    <div class="tagline__line">Die <span class="tagline__big">Trainingsakademie</span></div>
    <div class="tagline__line">aus der schönen Lüneburger Heide</div>
  </div>

  <div class="art art--stepper" role="img" aria-label="Illustration: Figur, die eine Stufe hinaufsteigt"></div>
  <div class="folio">10</div>
</section>

<section class="page page--right">
  <svg class="corner-bands" viewBox="0 0 150 160" aria-hidden="true">
    <polygon points="0,0 20,0 95,75 0,150" fill="url(#bandFade)"/>
    <polygon points="30,0 60,0 140,80 60,160 0,160 0,140 60,80" fill="url(#bandFade)" opacity="0.8"/>
  </svg>

  <div class="brand-name">Velmora Coaching</div>

  <div class="contact">
    <div class="contact__group">
      Kontakt:<br>
      Velmora Coaching<br>
      Henrike Velmora<br>
      Am Lindenhof 7<br>
      29600 Heidewald
    </div>
    <div class="contact__group">
      Telefon: 05100 - 12 345 67<br>
      Mobil: 0170 - 00 111 22
    </div>
    <div class="contact__group">kontakt@velmora-coaching.example</div>
  </div>

  <div class="tagline-glow"></div>
  <div class="tagline-rule-h"></div>
  <div class="tagline-rule-v"></div>
  <div class="tagline">
    <div class="tagline__line">„Velmora Coaching“</div>
    <div class="tagline__line">Die <span class="tagline__big">Trainingsakademie</span></div>
    <div class="tagline__line">aus der schönen Lüneburger Heide</div>
  </div>

  <div class="folio">11</div>
</section>

</body>
</html>
```